Modern Stationary for Architecs
Orbit Architecs
Simple
Arch. Fahad Nabil Alqurashi
CEO
KSA
Riyadh
Alwurud -Prince Faisal Road
eng.qurashi@postvela.net
We are looking for a professional and attractive for our Stationary .
so we expect to see :
Letterhead
envelop
CD label & Jacket
Folder
Just logo
logo
Please us this file for all stationary
Please use this file in Letterhead ONLY

```html
<!DOCTYPE html>
<html lang="en">
<head>
<meta charset="utf-8">
<title>Orbit Architecs – Business Card</title>
<link href="https://fonts.googleapis.com/css2?family=Source+Sans+3:wght@400;600&display=swap" rel="stylesheet">
<style>
  :root {
    --stage: #d9d9d9;
    --card: #f6f6f6;
    --card-edge: #e4e4e4;
    --ink: #3a3a3a;
    --ink-soft: #6d6d6d;
    --brand-red: #a31a22;
    --brand-red-dark: #7d1018;
  }
  * { margin: 0; padding: 0; box-sizing: border-box; }
  html, body { width: 1200px; height: 901px; overflow: hidden; }
  body {
    background: var(--stage);
    font-family: "Source Sans 3", sans-serif;
    color: var(--ink);
    display: flex;
    flex-direction: column;
    align-items: center;
    justify-content: center;
    gap: 40px;
  }
  .card {
    position: relative;
    width: 700px;
    height: 400px;
    border-radius: 26px;
    background: linear-gradient(135deg, #ffffff 0%, var(--card) 55%, var(--card-edge) 100%);
    box-shadow: 0 10px 28px rgba(0,0,0,0.18);
    overflow: hidden;
  }
  .brand {
    display: flex;
    align-items: center;
    gap: 12px;
  }
  .brand-dot {
    width: 18px; height: 18px;
    border-radius: 50%;
    background: var(--brand-red);
  }
  .brand-name {
    font-weight: 600;
    color: var(--ink-soft);
    letter-spacing: 0.5px;
  }
  /* back */
  .card-back .brand {
    position: absolute;
    left: 50%; top: 50%;
    transform: translate(-50%, -50%);
  }
  .card-back .brand-name { font-size: 44px; }
  .card-back .brand-dot { width: 26px; height: 26px; }
  /* front */
  .card-front .brand { position: absolute; left: 70px; top: 58px; }
  .card-front .brand-name { font-size: 36px; }
  .accent-band {
    position: absolute;
    left: 0; top: 150px;
    width: 22px; height: 210px;
    border-radius: 0 14px 14px 0;
    background: linear-gradient(180deg, var(--brand-red) 0%, var(--brand-red-dark) 100%);
  }
  .address {
    position: absolute;
    left: 58px; top: 168px;
    font-size: 15px;
    line-height: 21px;
  }
  .contact-list {
    position: absolute;
    left: 58px; top: 246px;
    list-style: none;
    font-size: 15px;
    line-height: 21px;
  }
  .contact-list li { display: flex; align-items: center; gap: 9px; }
  .contact-list svg { width: 14px; height: 14px; fill: var(--brand-red); flex: none; }
  .person {
    position: absolute;
    right: 44px; top: 206px;
    text-align: right;
  }
  .person-name { color: var(--brand-red); font-size: 18px; font-weight: 600; }
  .person-role { color: var(--ink-soft); font-size: 14px; margin-top: 2px; }
</style>
</head>
<body>
  <section class="card card-back">
    <div class="brand">
      <span class="brand-dot"></span>
      <span class="brand-name">Orbit Architecs</span>
    </div>
  </section>

  <section class="card card-front">
    <div class="brand">
      <span class="brand-dot"></span>
      <span class="brand-name">Orbit Architecs</span>
    </div>
    <div class="accent-band"></div>
    <address class="address" style="font-style:normal">
      KSA<br>Riyadh<br>Alwurud -Prince Faisal Road
    </address>
    <ul class="contact-list">
      <li>
        <svg viewBox="0 0 16 16"><path d="M3 2h3l1.5 3.5-2 1.3a9 9 0 0 0 3.7 3.7l1.3-2L14 10v3a1 1 0 0 1-1 1A12 12 0 0 1 2 3a1 1 0 0 1 1-1z"/></svg>
        00966114408271
      </li>
      <li>
        <svg viewBox="0 0 16 16"><path d="M5 1h6a1 1 0 0 1 1 1v12a1 1 0 0 1-1 1H5a1 1 0 0 1-1-1V2a1 1 0 0 1 1-1zm0 2v9h6V3zm3 10a.8.8 0 1 0 0 .01z"/></svg>
        966500731942
      </li>
      <li>
        <svg viewBox="0 0 16 16"><path d="M4 1h6v4H4zM2 6h12a1 1 0 0 1 1 1v5a1 1 0 0 1-1 1h-2v2H4v-2H2a1 1 0 0 1-1-1V7a1 1 0 0 1 1-1zm3 5v3h6v-3z"/></svg>
        0096611440827
      </li>
      <li>
        <svg viewBox="0 0 16 16"><path d="M1 3h14v10H1zm1.5 1.5v.3L8 8.6l5.5-3.8v-.3zm0 2.1v4.9h11V6.6L8 10.4z"/></svg>
        eng.qurashi@postvela.net
      </li>
    </ul>
    <div class="person">
      <div class="person-name">Arch. Fahad Nabil Alqurashi</div>
      <div class="person-role">CEO</div>
    </div>
  </section>
</body>
</html>
```